We are needing a bookcover for a reprint of our book "Whispers Beneath the Cobalt Ridgelands". It takes a look at the geologic formation found in the great plains. Our original cover was colorful and showed rock layers. Something similar but different and eye catching would be great. a geologic cross section showing various layers or possibly some different rocks/soils. We are really open to suggestions attached is the current book cover with the colored layers and the cover from the 80s.

Target Market(s)

Adult Readers

Industry/Entity Type

Nonprofit retail - science - nature

Requirements
Must have
• Geology or rock layers
Nice to have
• Books title, Geologic cross section
Should not have
• People or animals, no photos prefer sketch

```html
<!DOCTYPE html>
<html lang="en">
<head>
<meta charset="UTF-8">
<title>Whispers Beneath the Cobalt Ridgelands — Book Cover</title>
<link rel="stylesheet" href="https://fonts.googleapis.com/css2?family=Libre+Baskerville:wght@400;700&display=swap">
<style>
  :root {
    --cover-bg: #fcfcfb;
    --ink: #2e2110;
    --grass: #7fb540;
    --topsoil: #8a5a2b;
    --sand: #efb54a;
    --cobalt: #5b88ad;
    --stone: #8d8a86;
    --clay: #d2532a;
    --bedrock: #5f5e5c;
  }
  html, body {
    margin: 0;
    padding: 0;
    width: 900px;
    height: 1200px;
    overflow: hidden;
    background: var(--cover-bg);
  }
  .book-cover {
    position: relative;
    width: 900px;
    height: 1200px;
    background: var(--cover-bg);
    color: var(--ink);
    font-family: "Libre Baskerville", Georgia, serif;
  }
  .title {
    position: absolute;
    top: 72px;
    left: 0;
    width: 100%;
    margin: 0;
    text-align: center;
    font-weight: 400;
  }
  .title-kicker {
    display: block;
    font-size: 40px;
    letter-spacing: 0.5px;
    text-transform: uppercase;
    line-height: 1;
  }
  .title-main {
    display: block;
    margin-top: 44px;
    font-size: 86px;
    font-weight: 700;
    line-height: 1;
    letter-spacing: -0.5px;
  }
  .cross-section {
    position: absolute;
    left: 163px;
    top: 258px;
    width: 593px;
    height: 762px;
    border-radius: 6px;
    background: linear-gradient(
      to bottom,
      var(--grass) 0%,
      var(--grass) 8%,
      var(--topsoil) 13%,
      var(--sand) 20%,
      var(--sand) 27%,
      var(--cobalt) 31%,
      var(--cobalt) 37%,
      var(--stone) 42%,
      var(--stone) 52%,
      var(--clay) 57%,
      var(--clay) 67%,
      var(--bedrock) 74%,
      var(--bedrock) 100%
    );
  }
  .author {
    position: absolute;
    top: 1090px;
    left: 0;
    width: 100%;
    margin: 0;
    text-align: center;
    font-size: 40px;
    font-weight: 400;
    letter-spacing: 0.5px;
    text-transform: uppercase;
    line-height: 1;
  }
</style>
</head>
<body>
  <main class="book-cover">
    <h1 class="title">
      <span class="title-kicker">Whispers Beneath the</span>
      <span class="title-main">Cobalt Ridgelands</span>
    </h1>
    <div class="cross-section" role="img" aria-label="Hand-sketched geologic cross section: tufts of prairie grass on top, then brown topsoil, golden sand, cracked blue stone, grey boulders, red clay and dark grey bedrock blocks, split down the middle by a slanting fault line with small grass sprigs in the layers"></div>
    <p class="author">Author's Name</p>
  </main>
</body>
</html>
```